I need 7 images in certain sizes for an upcoming event

I an hosting an Radiant honors program and need 7 images for different marketing avenues. I would like to use my phone and event logo, but need it in 8 different sizes:
1. Marquee pic needs to be 3480 X 400px (minimum 696X80px)
This one needs my pic logo and event date of June 30, 2019

2.Mobile image size 1920X1080px showing my picture and the words Trailblazers: Radiant Quillonites Brisbury Centre
3. Desktop image: size 1920 X 50px with my pic and words below left corner TRAILBLAZERS: Radiant Quillonites Brisbury Centre

4. Event listing size: 500x250px
5. Hero Image 605xvariable height should not exceed a square picture only no logo.

6. Side marquee screen: 840X400px (minimum 168X80px)
include my pic, Use Words TRAILBLAZERS: Radiant Quillonites no logo and include words June 30 Brisbury Centre

7. last image size 2426x1365px My picture only no logo.
8. Facebook image size 1200x628px no text, no logo just my picture.
9. image size 410x305px - I want the logo used only. no dates and don't use my picture. Just the Radiant Quillonites logo in size 410X305
I attached the image flyer with all the sizes that I need. I need within the next 3 days. I need my picture in the image size on the flyer.

```html
<!DOCTYPE html>
<html lang="en">
<head>
<meta charset="utf-8">
<title>Trailblazers: Radiant Quillonites — Event Image Set</title>
<link rel="stylesheet" href="https://fonts.googleapis.com/css2?family=Roboto+Condensed:wght@400;900&family=Open+Sans:wght@400&display=swap">
<style>
  :root {
    --page: #ffffff;
    --panel: #a2a5ad;
    --ink: #000000;
    --photo-top: #b8875a;
    --photo-mid: #3a3433;
    --photo-bottom: #121112;
    --badge: #c99a2e;
  }
  * { box-sizing: border-box; margin: 0; padding: 0; }
  html, body {
    width: 1200px; height: 1200px; overflow: hidden;
    background: var(--page);
  }
  .sheet { position: relative; width: 1200px; height: 1200px; }
  .panel { position: absolute; background: var(--panel); overflow: hidden; }
  .portrait {
    position: absolute;
    background: linear-gradient(180deg, var(--photo-top) 0%, var(--photo-mid) 30%, var(--photo-bottom) 100%);
    border-radius: 40% 40% 0 0 / 14% 14% 0 0;
  }
  .headline {
    position: absolute;
    text-align: center;
    font-family: "Roboto Condensed", "Arial Narrow", sans-serif;
    color: var(--ink);
    transform: translateX(-50%);
    white-space: nowrap;
  }
  .headline .title { font-weight: 900; display: block; }
  .headline .line { font-weight: 400; display: block; }

  /* Mobile hero */
  .panel--hero { left: 16px; top: 18px; width: 1168px; height: 658px; }
  .panel--hero .portrait { left: 116px; top: 16px; width: 340px; height: 642px; }
  .panel--hero .headline { left: 784px; top: 120px; font-size: 76px; line-height: 108px; }
  .panel--hero .title { font-size: 84px; }

  /* Logo tile */
  .panel--logo { left: 84px; top: 700px; width: 328px; height: 244px; }
  .brand {
    position: absolute; left: 0; right: 0; top: 96px;
    display: flex; align-items: center; justify-content: center; gap: 10px;
    font-family: "Open Sans", sans-serif; font-weight: 400;
    font-size: 34px; letter-spacing: 1px; color: var(--ink);
  }
  .brand-dot { width: 26px; height: 26px; border-radius: 50%; background: var(--badge); flex: none; }

  /* Side marquee */
  .panel--marquee { left: 496px; top: 700px; width: 672px; height: 320px; }
  .panel--marquee .portrait { left: 72px; top: 8px; width: 220px; height: 312px; }
  .panel--marquee .headline { left: 488px; top: 40px; font-size: 36px; line-height: 48px; }
  .panel--marquee .title { font-size: 38px; }
  .panel--marquee .date { display: block; margin-top: 52px; font-weight: 400; font-size: 40px; }

  /* Event listing */
  .panel--listing { left: 48px; top: 968px; width: 400px; height: 200px; }
  .panel--listing .portrait { left: 48px; top: 12px; width: 124px; height: 188px; }
  .panel--listing .headline { left: 280px; top: 40px; font-size: 22px; line-height: 29.6px; }
  .panel--listing .title { font-size: 22px; }
</style>
</head>
<body>
<main class="sheet">

  <section class="panel panel--hero">
    <div class="portrait" role="img" aria-label="Photo of the host standing, hand on hip, in a black sequinned outfit"></div>
    <h1 class="headline">
      <span class="title">Trailblazers:</span>
      <span class="line">Radiant Quillonites</span>
      <span class="line">Brisbury</span>
      <span class="line">Centre</span>
    </h1>
  </section>

  <section class="panel panel--logo">
    <div class="brand"><span class="brand-dot"></span><span>TRAILBLAZERS</span></div>
  </section>

  <section class="panel panel--marquee">
    <div class="portrait" role="img" aria-label="Photo of the host standing, hand on hip, in a black sequinned outfit"></div>
    <h2 class="headline">
      <span class="title">Trailblazers:</span>
      <span class="line">Radiant Quillonites</span>
      <span class="line">Brisbury Centre</span>
      <span class="date">June 30, 2019</span>
    </h2>
  </section>

  <section class="panel panel--listing">
    <div class="portrait" role="img" aria-label="Photo of the host standing, hand on hip, in a black sequinned outfit"></div>
    <h2 class="headline">
      <span class="title">Trailblazers:</span>
      <span class="line">Radiant Quillonites</span>
      <span class="line">Brisbury</span>
      <span class="line">Centre</span>
    </h2>
  </section>

</main>
</body>
</html>
```